Business Card Design for a Sound engineer and DJ

We would like a residn of the business card.

Logo must remain the same.
The card is for the owner of the company.
The business card is in Arabic as the company is based in Kuwait.
The company specializes in sound engineering for singers concerts and events and in addition DJ.
The color options is up to the designer but we would like it masculine as the owner is a man.

Target Market(s)

All ages

Industry/Entity Type

Media

Contact Information for Business Card

Name:
Eng. Tarek Halabi
م/طارق حلبي

The name above is in Arabic and English.

Title: General Manager
Mobile: +965 66307852
Office: +965 22486037
Email: info@sawtarin.net

Address:
Office no. 3
1st floor
Almarfa Complex
Rashed AlQeblawi St.
Salmiya
Kuwait

Instagram: @sawtarin
Snap: sawtarin

Requirements
Nice to have
• can we have Instagram icon and snap icon and a phone vector and email?
• Instead of writing the words

```html
<!DOCTYPE html>
<html lang="en">
<head>
<meta charset="utf-8">
<title>Sawtarin Business Card</title>
<link rel="stylesheet" href="https://fonts.googleapis.com/css2?family=Open+Sans:wght@400;600;700&family=Cairo:wght@400;600;700&display=swap">
<style>
  :root {
    --stage: #2b2b2d;
    --card-light: #ffffff;
    --card-dark: #050407;
    --purple: #8a3fa8;
    --magenta: #c43a93;
    --violet: #6c5bc4;
    --sky: #5cc2ee;
    --text-light: #f1eef6;
    --muted-purple: #7a4f96;
  }
  * { box-sizing: border-box; margin: 0; padding: 0; }
  html, body { width: 1200px; height: 900px; overflow: hidden; }
  body {
    background: var(--stage);
    font-family: "Open Sans", sans-serif;
    display: flex;
    flex-direction: column;
    align-items: center;
    justify-content: center;
    gap: 44px;
  }
  .card {
    width: 700px;
    height: 400px;
    border-radius: 22px;
    position: relative;
    overflow: hidden;
  }
  .card--front { background: var(--card-light); }
  .card--back { background: var(--card-dark); }

  .brand {
    position: absolute;
    display: flex;
    flex-direction: column;
  }
  .card--front .brand { left: 56px; top: 120px; }
  .card--back .brand { left: 44px; top: 110px; }

  .brand__name {
    font-family: "Open Sans", sans-serif;
    font-weight: 400;
    color: var(--purple);
    letter-spacing: 0.32em;
    text-transform: uppercase;
  }
  .card--front .brand__name { font-size: 46px; }
  .card--back .brand__name { font-size: 34px; color: var(--magenta); }

  .brand__tagline {
    font-size: 15px;
    letter-spacing: 0.18em;
    color: var(--purple);
    margin-top: 6px;
  }
  .card--back .brand__tagline { font-size: 12px; color: #b79ad0; }

  .brand__tagline-ar {
    font-family: "Cairo", sans-serif;
    font-size: 20px;
    color: var(--purple);
    direction: rtl;
    text-align: left;
    margin-top: 2px;
  }
  .card--back .brand__tagline-ar { font-size: 16px; color: #b79ad0; }

  .socials {
    display: flex;
    gap: 30px;
    margin-top: 18px;
    font-size: 18px;
    color: var(--purple);
  }
  .socials__item { display: flex; align-items: center; gap: 8px; }
  .socials__mark { width: 14px; height: 14px; background: var(--sky); }
  .socials__mark--round { border-radius: 50%; }

  .contact {
    position: absolute;
    right: 40px;
    top: 48px;
    text-align: right;
    color: var(--text-light);
  }
  .contact__name-ar {
    font-family: "Cairo", sans-serif;
    font-weight: 600;
    font-size: 40px;
    line-height: 1.1;
    color: var(--sky);
    direction: rtl;
  }
  .contact__name-en {
    font-weight: 700;
    font-size: 26px;
    color: var(--purple);
    margin-top: 2px;
  }
  .contact__title { font-size: 17px; margin-top: 4px; }
  .contact__lines { list-style: none; margin-top: 8px; font-size: 17px; line-height: 1.35; }
  .contact__lines li { display: flex; justify-content: flex-end; align-items: center; gap: 8px; }
  .contact__lines svg { width: 15px; height: 15px; stroke: var(--text-light); fill: none; stroke-width: 1.6; }
  .contact__address { margin-top: 8px; font-size: 17px; line-height: 1.35; }
</style>
</head>
<body>
  <section class="card card--front" aria-label="Card front">
    <div class="brand">
      <span class="brand__name">Sawtarin</span>
      <span class="brand__tagline">DJ - SOUND ENG. - LIGHTING</span>
      <span class="brand__tagline-ar">دي جي - هندسة صوت - إضاءة</span>
      <div class="socials">
        <span class="socials__item"><span class="socials__mark"></span>@sawtarin</span>
        <span class="socials__item"><span class="socials__mark socials__mark--round"></span>sawtarin</span>
      </div>
    </div>
  </section>

  <section class="card card--back" aria-label="Card back">
    <div class="brand">
      <span class="brand__name">Sawtarin</span>
      <span class="brand__tagline">DJ - SOUND ENG. - LIGHTING</span>
      <span class="brand__tagline-ar">دي جي - هندسة صوت - إضاءة</span>
    </div>
    <div class="contact">
      <p class="contact__name-ar">م/طارق حلبي</p>
      <p class="contact__name-en">Eng. Tarek Halabi</p>
      <p class="contact__title">General Manager</p>
      <ul class="contact__lines">
        <li>+965 66307852
          <svg viewBox="0 0 16 16"><rect x="4" y="1.5" width="8" height="13" rx="1.5"/><line x1="7" y1="12" x2="9" y2="12"/></svg>
        </li>
        <li>+965 22486037
          <svg viewBox="0 0 16 16"><path d="M3 2.5l3 .5 1 3-1.6 1.2a8 8 0 0 0 3.4 3.4L10 9l3 1 .5 3-1.5 1.5A11 11 0 0 1 1.5 4z"/></svg>
        </li>
        <li>info@sawtarin.net
          <svg viewBox="0 0 16 16"><rect x="1.5" y="3.5" width="13" height="9" rx="1"/><polyline points="1.5,4 8,9 14.5,4"/></svg>
        </li>
      </ul>
      <p class="contact__address">Office no. 3<br>1st floor Almarfa Complex<br>Rashed AlQeblawi St. Salmiya Kuwait</p>
    </div>
  </section>
</body>
</html>
```